Unique and original Business Card for Financial Services Business

I have moved premises and need to change the detail on my business card so thought now is a good time for a re-design. Looking for something professional and modern with colours to fit in with out logo. Like the idea of foil or embossing if that works but not a must have but I do want something that stands out and that I could not design myself.

Once business card is designed I will also be looking to get letterhead and flyers done but want the business card concept in place first.

The majority of designs I am receiving are generic and template based. I am looking for something unique and original. We have some great design elements in our logo, think outside the box and show me something that stands out from the crowd.

Target Market(s)

Business Professionals

Industry/Entity Type

Finance

Contact Information for Business Card

Name: Delia Norwood Phone 0473 958 162 Address PO Box 8617 Mossvale NSW 2389 Email info@steadyharbourfinancialservices.com.au website www.steadyharbourfinancialservices.com.au

Font styles to use
Other font styles liked:
• Ralway

Requirements
Should not have
• No black backgrounds please

```html
<!DOCTYPE html>
<html lang="en">
<head>
<meta charset="utf-8">
<title>Steady Harbour Financial Services – Business Card</title>
<link rel="stylesheet" href="https://fonts.googleapis.com/css2?family=Montserrat:ital,wght@0,400;0,600;0,700;1,800&family=Raleway:wght@300;400&display=swap">
<style>
  :root{
    --stage:#e6e9ec;
    --paper:#ffffff;
    --teal:#11878f;
    --navy:#0b5677;
    --charcoal:#3b3c3f;
    --slate:#2d2f33;
    --mist:#dfe2e4;
    --ink:#ffffff;
    --logo:#1a8e96;
  }
  *{box-sizing:border-box;margin:0;padding:0}
  html,body{width:1200px;height:780px;overflow:hidden}
  body{background:var(--stage);font-family:"Montserrat",sans-serif;position:relative}

  .card{position:absolute;top:236px;width:540px;height:309px;border-radius:18px;overflow:hidden;background:var(--paper);box-shadow:0 10px 28px rgba(20,30,40,.22)}
  .card--front{left:45px}
  .card--back{left:615px}

  /* front */
  .front__photo{position:absolute;left:0;top:0;width:100%;height:170px;background:linear-gradient(180deg,#fafafa 0%,#e9eaeb 55%,#d9dbdd 100%)}
  .brand{position:absolute;display:flex;align-items:center;gap:12px;font-family:"Raleway",sans-serif;font-weight:300;color:var(--logo)}
  .brand__mark{width:30px;height:30px;background:var(--logo);flex:none}
  .brand__name{line-height:1.05;letter-spacing:.5px}
  .card--front .brand{left:150px;top:52px;font-size:28px}
  .card--front .brand__mark{width:40px;height:40px}
  .brand__sub{display:block;font-size:.5em;letter-spacing:.35em;margin-top:4px}
  .front__band{position:absolute;left:0;top:170px;width:100%;height:58px;background:var(--navy);display:flex;align-items:center;gap:10px;padding-left:34px;color:var(--ink);font-weight:600;font-size:17.5px;letter-spacing:.2px}
  .front__base{position:absolute;left:0;top:228px;width:100%;height:81px;background:var(--charcoal)}

  /* back */
  .back__photo{position:absolute;left:0;top:62px;width:100%;height:62px;background:linear-gradient(90deg,#1f2124,#4a4c50 60%,#2a2c2f)}
  .back__teal{position:absolute;left:0;top:104px;width:100%;height:205px;background:var(--teal);clip-path:polygon(0 0,58% 0,66% 40%,100% 40%,100% 100%,0 100%)}
  .card--back .brand{left:150px;top:12px;font-size:19px}
  .card--back .brand__mark{width:30px;height:30px}
  .contact{position:absolute;left:22px;top:118px;list-style:none;color:var(--ink);font-size:10.5px}
  .contact li{display:flex;align-items:center;gap:9px;margin-bottom:8px}
  .icon{width:20px;height:20px;border-radius:50%;background:var(--navy);display:flex;align-items:center;justify-content:center;flex:none}
  .name-tab{position:absolute;right:0;top:150px;width:210px;height:62px;background:var(--navy);color:var(--ink);padding:10px 0 0 18px}
  .name-tab__name{font-weight:800;font-style:italic;font-size:22px;text-transform:uppercase;letter-spacing:-.3px}
  .name-tab__role{font-size:9.5px;font-weight:600;letter-spacing:1px;text-transform:uppercase;margin-top:2px}
  .phone{position:absolute;left:238px;top:232px;display:flex;align-items:center;gap:10px;color:var(--ink)}
  .phone .icon{width:32px;height:32px}
  .phone__label{font-size:10px;font-weight:600;letter-spacing:3px;text-transform:uppercase}
  .phone__number{font-size:23px;font-weight:700;line-height:1.1}
</style>
</head>
<body>

<section class="card card--front">
  <div class="front__photo" role="img" aria-label="Faded black and white city skyline photograph"></div>
  <div class="brand">
    <span class="brand__mark"></span>
    <span class="brand__name">STEADY HARBOUR<span class="brand__sub">Financial Services</span></span>
  </div>
  <div class="front__band">
    <svg width="15" height="15" viewBox="0 0 16 16" fill="none" stroke="#fff" stroke-width="1.5"><circle cx="8" cy="8" r="6.5"/><ellipse cx="8" cy="8" rx="3" ry="6.5"/><path d="M1.5 8h13"/></svg>
    <span class="front__url">www.steadyharbourfinancialservices.com.au</span>
  </div>
  <div class="front__base"></div>
</section>

<section class="card card--back">
  <div class="back__photo" role="img" aria-label="Dark city skyline photograph band"></div>
  <div class="back__teal"></div>
  <div class="brand">
    <span class="brand__mark"></span>
    <span class="brand__name">STEADY HARBOUR<span class="brand__sub">Financial Services</span></span>
  </div>
  <ul class="contact">
    <li><span class="icon"><svg width="10" height="8" viewBox="0 0 10 8"><rect x=".5" y=".5" width="9" height="7" fill="none" stroke="#fff"/><path d="M.5 .5 5 4.5 9.5 .5" fill="none" stroke="#fff"/></svg></span>info@steadyharbourfinancialservices.com.au</li>
    <li><span class="icon"><svg width="11" height="11" viewBox="0 0 16 16" fill="none" stroke="#fff" stroke-width="1.6"><circle cx="8" cy="8" r="6.5"/><ellipse cx="8" cy="8" rx="3" ry="6.5"/><path d="M1.5 8h13"/></svg></span>www.steadyharbourfinancialservices.com.au</li>
    <li><span class="icon"><svg width="10" height="10" viewBox="0 0 10 10"><path d="M9 1 1 4.5 4.5 5.5 5.5 9Z" fill="#fff"/></svg></span>PO Box 8617 Mossvale NSW 2389</li>
  </ul>
  <div class="name-tab">
    <div class="name-tab__name">Delia Norwood</div>
    <div class="name-tab__role">Graphic Designer</div>
  </div>
  <div class="phone">
    <span class="icon"><svg width="14" height="14" viewBox="0 0 24 24"><path fill="#fff" d="M6.6 10.8a15 15 0 0 0 6.6 6.6l2.2-2.2c.3-.3.7-.4 1-.2 1.1.4 2.3.6 3.6.6.6 0 1 .4 1 1V20c0 .6-.4 1-1 1A17 17 0 0 1 3 4c0-.6.4-1 1-1h3.5c.6 0 1 .4 1 1 0 1.3.2 2.5.6 3.6.1.3 0 .7-.2 1z"/></svg></span>
    <div>
      <div class="phone__label">Contact Info</div>
      <div class="phone__number">0473 958 162</div>
    </div>
  </div>
</section>

</body>
</html>
```